Bramblecrest Roofing Co. business card design

I am a Roofing contractor in Texas. The name of my company is Bramblecrest Roofing Co. I also offer a few other services (Christmas light installation, gutters, fencing, pressure washing). However my main gig is roofing. Storm restoration and knowledge of the insurance claim process is my specialty.

My colors are black, red and white. I’d like something pretty simple and clean. Modern looking but with a splash of this red tartan pattern.

I have another version of my logo being edited at the moment where the little top part of the F in roofing that’s currently tartan will be changed to just solid red to make it more visible. So if that’s something you can change in your mock up great. But I can provide the full version once the contest is complete

Target Market(s)

Homeowners

Industry/Entity Type

Roofing

Contact Information for Business Card

Darren Pike. 682-555-0193. www.bramblecrest roofing.example Darren@bramblecrestroofing.example

Colors
EB3D1F
EC4F4E
F09395
F8D3D4
FCEDEE

Requirements
Nice to have
• Maybe instead of a business address. I could say serving all DFW Texas or something like that. And maybe add a line somewhere saying deductible assistance? Just a thought

```html
<!DOCTYPE html>
<html lang="en">
<head>
<meta charset="utf-8">
<title>Bramblecrest Roofing Co. — Business Card</title>
<link rel="stylesheet" href="https://fonts.googleapis.com/css2?family=Lato:wght@400;700;900&family=Michroma&display=swap">
<style>
  :root {
    --red: #d90b0b;
    --red-deep: #a00808;
    --red-dark: #7d0606;
    --red-text: #d81414;
    --pink: #fcedee;
    --pink-mid: #f8d3d4;
    --ink: #111111;
    --paper: #ffffff;
    --grey-band: #ececec;
    --grey-square: #bdbdbd;
    --stage: #2a2a2a;
  }
  * { box-sizing: border-box; margin: 0; padding: 0; }
  html, body { width: 1200px; height: 800px; overflow: hidden; background: var(--stage); }
  .canvas { position: relative; width: 1200px; height: 800px; }

  .card {
    position: absolute; left: 290px; width: 620px; height: 354px;
    border-radius: 18px; overflow: hidden;
    box-shadow: 0 10px 28px rgba(0,0,0,.45);
  }
  .card-front { top: 28px; background: var(--red); }
  .card-back  { top: 418px; background: var(--paper); }

  .band { position: absolute; }

  /* front bands */
  .card-front .band-h { left: 0; right: 0; top: 60px; height: 50px; background: var(--red-deep); }
  .card-front .band-v { top: 0; bottom: 0; left: 500px; width: 50px; background: var(--red-deep); }
  .card-front .band-square { left: 500px; top: 60px; width: 50px; height: 50px; background: #000; }
  .card-front .band-edge-v { top: 0; bottom: 0; left: 22px; width: 34px; background: rgba(120,0,0,.35); }
  .card-front .band-edge-h { left: 0; right: 0; top: 298px; height: 30px; background: rgba(120,0,0,.35); }

  .front-brand {
    position: absolute; left: 110px; top: 130px;
    display: flex; align-items: center; gap: 22px;
  }
  .brand-mark {
    width: 96px; height: 96px; border-radius: 50%;
    background: var(--paper); flex: none;
  }
  .front-brand .brand-name {
    font-family: "Lato", sans-serif; font-weight: 900;
    color: var(--paper); font-size: 34px; line-height: 1.05;
    letter-spacing: 1px; text-transform: uppercase;
  }

  /* back bands */
  .card-back .band-h { left: 0; right: 0; top: 40px; height: 46px; background: var(--grey-band); }
  .card-back .band-v { top: 0; bottom: 0; left: 505px; width: 46px; background: var(--grey-band); }
  .card-back .band-square { left: 505px; top: 0; width: 46px; height: 40px; background: var(--grey-square); }
  .card-back .band-pink-v { top: 0; bottom: 0; left: 22px; width: 34px; background: var(--pink); }
  .card-back .band-pink-h { left: 0; right: 0; top: 258px; height: 30px; background: var(--pink); }

  .back-brand {
    position: absolute; right: 30px; top: 18px;
    display: flex; flex-direction: column; align-items: flex-end; gap: 10px;
  }
  .back-brand .brand-mark { width: 82px; height: 82px; background: var(--red); margin-right: 40px; }
  .back-brand .brand-name {
    font-family: "Lato", sans-serif; font-weight: 900;
    color: var(--red-text); font-size: 22px; line-height: 1.1;
    text-transform: uppercase; text-align: right; letter-spacing: .5px;
  }

  .person { position: absolute; left: 60px; top: 160px; }
  .person-name {
    font-family: "Michroma", sans-serif; font-size: 27px;
    color: var(--ink); letter-spacing: 1px; text-transform: uppercase;
  }
  .person-title {
    font-family: "Lato", sans-serif; font-size: 17px; color: var(--red-text); margin-top: 2px;
  }

  .divider { position: absolute; left: 60px; right: 36px; top: 224px; height: 1.5px; background: var(--ink); }

  .contacts {
    position: absolute; left: 60px; top: 236px; list-style: none;
    font-family: "Lato", sans-serif; color: var(--ink);
  }
  .contacts li { display: flex; align-items: center; gap: 9px; height: 24px; font-size: 14px; }
  .contacts li.phone { font-size: 18px; }
  .contacts svg { width: 14px; height: 14px; flex: none; }

  .office {
    position: absolute; right: 36px; top: 236px; text-align: right;
    font-family: "Lato", sans-serif; color: var(--ink); font-size: 14px; line-height: 1.5;
  }
  .office-name { color: var(--red-text); font-size: 17px; }

  .footer-black { position: absolute; left: 0; bottom: 0; width: 470px; height: 16px; background: var(--ink); clip-path: polygon(0 0, 100% 0, 96% 100%, 0 100%); }
  .footer-red { position: absolute; right: 0; bottom: 0; width: 170px; height: 22px; background: var(--red); clip-path: polygon(8% 0, 100% 0, 100% 100%, 0 100%); }
</style>
</head>
<body>
<main class="canvas">

  <section class="card card-front" aria-label="Card front">
    <div class="band band-edge-v"></div>
    <div class="band band-edge-h"></div>
    <div class="band band-h"></div>
    <div class="band band-v"></div>
    <div class="band band-square"></div>
    <div class="front-brand">
      <div class="brand-mark"></div>
      <p class="brand-name">Bramblecrest<br>Roofing Co.</p>
    </div>
  </section>

  <section class="card card-back" aria-label="Card back">
    <div class="band band-pink-v"></div>
    <div class="band band-pink-h"></div>
    <div class="band band-h"></div>
    <div class="band band-v"></div>
    <div class="band band-square"></div>

    <div class="back-brand">
      <div class="brand-mark"></div>
      <p class="brand-name">Bramblecrest<br>Roofing Co.</p>
    </div>

    <div class="person">
      <h1 class="person-name">Darren Pike</h1>
      <p class="person-title">Founder &amp; CEO</p>
    </div>

    <div class="divider"></div>

    <ul class="contacts">
      <li class="phone">
        <svg viewBox="0 0 24 24" aria-hidden="true"><path fill="#d81414" d="M6.6 10.8a15 15 0 0 0 6.6 6.6l2.2-2.2c.3-.3.7-.4 1-.2 1.1.4 2.3.6 3.6.6.6 0 1 .4 1 1V20c0 .6-.4 1-1 1A17 17 0 0 1 3 4c0-.6.4-1 1-1h3.5c.6 0 1 .4 1 1 0 1.3.2 2.5.6 3.6.1.3 0 .7-.2 1z"/></svg>
        682-555-0193
      </li>
      <li>
        <svg viewBox="0 0 24 24" aria-hidden="true"><path fill="#d81414" d="M2 5h20v14H2z"/><path fill="none" stroke="#fff" stroke-width="1.6" d="M2.5 5.5 12 13l9.5-7.5"/></svg>
        Darren@bramblecrestroofing.example
      </li>
      <li>
        <svg viewBox="0 0 24 24" aria-hidden="true"><circle cx="12" cy="12" r="9.5" fill="none" stroke="#d81414" stroke-width="2"/><path fill="none" stroke="#d81414" stroke-width="1.6" d="M2.5 12h19M12 2.5c3 3 3 16 0 19M12 2.5c-3 3-3 16 0 19"/></svg>
        www.bramblecrest roofing.example
      </li>
    </ul>

    <address class="office" style="font-style:normal">
      <p class="office-name">Bramblecrest Roofing Co</p>
      <p>123 Anywhere St</p>
      <p>Any City, State 12345</p>
    </address>

    <div class="footer-black"></div>
    <div class="footer-red"></div>
  </section>

</main>
</body>
</html>
```